Packaging for Mia&Pom High quality baby teether and accessories

We need a packaging box with a front window for our baby teether line of product. The product line consists of different teether for baby. Safety, quality and design are our key features. We have proposed a color palette available in the photos but we would like to see some creative design with abstract forms. We are open to suggestions for the colors as long as the focus stays on the product inside the box. Design must be gender neutral as it is for boys and girls. Our product packaging need to be bilingual French and English with French being bigger(for the product name) then english in the design. You can play with our logo and adapt the color to fit your design(AI files have been provided).
Available files:
• Die Cut Template
• Logo (Adobe Illustrator)
• Color palette example
• Inspiration example
• Product pictures
• Abstract artsy design and colors
• Gender neutral
• NO ANIMALS
• NO Bright colors
• Textures and colors
• Embossed logo (shiny)
• Front window (transparent plastic) to be added on die cut template: rounded corners (measurement from each side: (suggestions)(top)20mmx(right)20mmx(left)20mmx(bottom)30mm
• Might be used for other products so must be easily adaptable
Here is what we should find on each side of the packaging: the way you present it is yours.
Front :
• Product name: Hochet de dentition / Rattle Teether
• Age : à partir de 6 mois / from 6 months
• Brand logo
Side 1:
• Disclaimer
• Bar code
• Importé par / imported by: Dorvan supplies inc.
o Granby, QC, Canada, K4M 7B2
• Conçu au Canada/Fabriqué en Chine
• Designed in Canada/Made in China
• CE logo
Back:
• Product advantages: with icons. Clean and refined (NOT jammed)
o Apprentissage/learning
o Doux sur les gencive/soft on gum
o Développement moteur/helps develop motricity
o Peut aider à Appaiser l’anxiété/Can help reduce anxiety
• Avantage conception:
o BPA free
o Phtalates free
o Lead Free
Back OR side
• Entretient/maintenance care:
o Nos produits sont faits de matériaux neufs seulement et de bois non traité. Nous recommandons le lavage à la main et le séchage à l’air libre. Our products are made from new material only and from untreated wood. We recommend hand washing and air drying.
Side 2:
• Could have a little something but should stay clean.
Botton:
• Blank
Target Market(s)
high end mass market, young family and friends. trendy products
Industry/Entity Type
Baby
Look and feel

```html
<!DOCTYPE html>
<html lang="fr">
<head>
<meta charset="utf-8">
<title>Mia&amp;Pom – Hochet de dentition</title>
<link rel="stylesheet" href="https://fonts.googleapis.com/css2?family=Lora:wght@400;600&family=Lato:wght@400;700&display=swap">
<style>
  :root {
    --bg: #dff2ea;
    --panel: #ffffff;
    --side-shade: #f4f6f4;
    --mint: #cdebdc;
    --blush: #e9d0cf;
    --sand: #efe3d3;
    --slate: #c9ccd6;
    --sage: #c9dccf;
    --gold: #b88b46;
    --green-text: #4f8a6b;
    --grey-text: #8d9893;
  }
  * { margin: 0; padding: 0; box-sizing: border-box; }
  html, body { width: 1200px; height: 1049px; overflow: hidden; }
  body {
    background: var(--bg);
    position: relative;
    font-family: "Lato", sans-serif;
  }
  .dieline { position: absolute; left: 325px; top: 150px; width: 550px; height: 700px; }
  .hang-tab {
    position: absolute; left: 170px; top: 0; width: 380px; height: 80px;
    background: var(--panel); border-radius: 6px 6px 0 0;
  }
  .hang-hole {
    position: absolute; left: 50%; top: 28px; width: 70px; height: 22px;
    transform: translateX(-50%); border-radius: 11px; background: var(--bg);
  }
  .side-panel {
    position: absolute; left: 0; top: 80px; width: 170px; height: 620px;
    background: var(--side-shade); overflow: hidden;
  }
  .front-panel {
    position: absolute; left: 170px; top: 80px; width: 380px; height: 620px;
    background: var(--panel); overflow: hidden;
  }
  .pastel-pattern {
    position: absolute; left: 0; bottom: 0; width: 100%; height: 380px;
    background: linear-gradient(180deg,
      rgba(239,227,211,0) 0%,
      var(--sand) 14%,
      var(--blush) 34%,
      var(--slate) 54%,
      var(--sage) 72%,
      var(--mint) 88%,
      var(--mint) 100%);
  }
  .disclaimer {
    position: relative; padding: 30px 18px 0; font-size: 7.5px; line-height: 1.45;
    color: var(--green-text);
  }
  .disclaimer p + p { margin-top: 8px; }
  .importer {
    position: absolute; left: 18px; right: 18px; bottom: 92px;
    font-size: 7px; line-height: 1.45; color: var(--green-text);
  }
  .ce-mark {
    position: absolute; right: 22px; bottom: 48px; width: 18px; height: 14px;
    border: 1.5px solid var(--grey-text); border-radius: 2px;
  }
  .brand {
    position: absolute; left: 0; right: 0; top: 30px;
    display: flex; align-items: center; justify-content: center; gap: 10px;
  }
  .brand-dot { width: 26px; height: 26px; border-radius: 50%; background: var(--gold); opacity: .85; }
  .brand-name {
    font-family: "Lora", serif; font-weight: 400; font-size: 30px;
    color: var(--gold); letter-spacing: .5px;
  }
  .window {
    position: absolute; left: 45px; top: 90px; width: 290px; height: 430px;
    border-radius: 26px; background: linear-gradient(180deg, #eef1ef 0%, #e3e8e5 100%);
    box-shadow: inset 0 0 0 2px rgba(255,255,255,.8);
    overflow: hidden;
  }
  .product-photo {
    position: absolute; left: 70px; top: 20px; width: 150px; height: 390px;
    border-radius: 70px 70px 60px 60px;
    background: linear-gradient(180deg, #8a8f8c 0%, #7c817e 65%, #d9bf98 85%, #c9ab82 100%);
    opacity: .9;
  }
  .product-name {
    position: absolute; left: 0; right: 0; bottom: 26px; text-align: center;
    font-family: "Lora", serif; color: var(--green-text);
  }
  .product-name .fr { font-size: 15px; font-weight: 600; }
  .product-name .en { font-size: 11px; font-weight: 400; }
  .product-age { font-size: 11px; margin-top: 3px; }
  .product-age .en { font-size: 9px; }
</style>
</head>
<body>
  <div class="dieline">
    <div class="hang-tab"><div class="hang-hole"></div></div>

    <section class="side-panel">
      <div class="pastel-pattern" role="img" aria-label="Motif abstrait de bandes pastel sable, rose, gris et menthe"></div>
      <div class="disclaimer">
        <p>Attention : toujours surveiller votre enfant pendant l'utilisation. Vérifier le produit avant chaque usage.</p>
        <p>Warning: always supervise your child during use. Check the product before each use and discard at first sign of damage. Keep this packaging for future reference.</p>
      </div>
      <div class="importer">
        Importé par / Imported by :<br>
        Dorvan supplies inc.<br>
        Granby, QC, Canada, K4M 7B2<br><br>
        Conçu au Canada / Fabriqué en Chine<br>
        Designed in Canada / Made in China
      </div>
      <div class="ce-mark" aria-hidden="true"></div>
    </section>

    <section class="front-panel">
      <div class="pastel-pattern" role="img" aria-label="Motif abstrait de bandes pastel sable, rose, gris et menthe"></div>

      <div class="brand">
        <span class="brand-dot"></span>
        <span class="brand-name">Mia&amp;Pom</span>
      </div>

      <div class="window">
        <div class="product-photo" role="img" aria-label="Photo du hochet de dentition en crochet gris avec anneau en bois"></div>
      </div>

      <div class="product-name">
        <div><span class="fr">Hochet de dentition</span> / <span class="en">Rattle Teether</span></div>
        <div class="product-age">à partir de 6 mois / <span class="en">from 6 months</span></div>
      </div>
    </section>
  </div>
</body>
</html>
```